Gymnastics and fitness web design

Varlow Gymnastics and fitness centre is opening a new branch in the United States.
Target Audience:
22 to 40 year old people who are not satisfied with their current body figure, shape and size.
and
Our programs
PulseLift, Sports performance and personal training
DESIGN STYLE:
We want the site to be trendy, edgy and cool. The colors we prefer are blue, black and silver. Th idea is people should get motivated by seeing our website. We don't like adding many text in the design, images oriented design is what we are after.
Contents should be added-
Slider
who we are?
section for our programs
Why us?
Video showing some tutorials
Articles
contact us form with map, Address, Phone number, timings, and social media buttons.

```html
<!DOCTYPE html>
<html lang="en">
<head>
<meta charset="utf-8">
<title>Varlow Gymnastics &amp; Fitness Centre – Latest News</title>
<link href="https://fonts.googleapis.com/css2?family=Russo+One&family=Exo+2:wght@500;600&family=Montserrat:wght@400;500;600&display=swap" rel="stylesheet">
<style>
  :root {
    --blue: #1e2fe6;
    --black: #000;
    --ink: #1d1d1d;
    --text: #3c3c3c;
    --page: #f1f1f1;
    --topbar: #e4e4e4;
    --white: #fff;
  }
  * { box-sizing: border-box; margin: 0; padding: 0; }
  html, body { width: 1200px; height: 1200px; overflow: hidden; }
  body { position: relative; background: var(--page); font-family: "Montserrat", sans-serif; color: var(--text); }
  .abs { position: absolute; }

  /* top info bar */
  .topbar { left: 0; top: 0; width: 1200px; height: 32px; background: var(--topbar); }
  .topbar .info { top: 6px; font-size: 7px; line-height: 8px; color: #555; white-space: nowrap; }
  .topbar .info strong { font-weight: 600; color: #333; }
  .topbar .divider { top: 5px; width: 1px; height: 21px; background: #bdbdbd; }
  .appointment { left: 792px; top: 2px; width: 152px; height: 24px; background: var(--blue); border-radius: 2px; color: var(--white);
    font-size: 9px; font-weight: 600; display: flex; align-items: center; justify-content: center; }

  /* navigation */
  .nav { left: 0; top: 32px; width: 1200px; height: 72px; background: var(--black); }
  .brand { left: 254px; top: 24px; display: flex; align-items: center; gap: 9px; }
  .brand-mark { width: 14px; height: 14px; background: var(--blue); }
  .brand-name { font-family: "Montserrat", sans-serif; font-weight: 600; font-size: 20px; line-height: 24px; color: var(--white); }
  .menu a { position: absolute; top: 29px; color: var(--white); font-size: 11.5px; font-weight: 500; text-decoration: none; }
  .menu a.active { top: 24px; border: 1px solid var(--blue); border-radius: 2px; width: 60px; height: 24px; display: flex; align-items: center; justify-content: center; }

  /* hero */
  .hero { left: 0; top: 104px; width: 1200px; height: 390px;
    background: linear-gradient(160deg, #3c3f52 0%, #272a3d 35%, #2f3560 65%, #3a45a8 100%); }
  .hero-title { left: 0; top: 98px; width: 1200px; text-align: center; font-family: "Russo One", sans-serif; font-size: 50px; color: var(--blue); letter-spacing: 3px; }
  .hero-sub { left: 0; top: 164px; width: 1200px; text-align: center; color: var(--white); font-size: 12px; line-height: 15.5px; font-weight: 500; }
  .tabs { left: 254px; top: 293px; width: 690px; height: 53px; background: rgba(150,150,165,0.45); border-radius: 3px; }
  .tab { top: 18px; width: 150px; text-align: center; font-family: "Russo One", sans-serif; font-size: 11px; color: var(--white); letter-spacing: 1px; }
  .tab-line { left: 39px; top: 39px; width: 113px; height: 2px; background: var(--blue); }

  /* articles */
  .card { background: var(--white); }
  .photo { position: absolute; }
  .title { font-family: "Exo 2", sans-serif; font-weight: 600; font-size: 19px; line-height: 18.5px; color: var(--ink); letter-spacing: 1.4px; text-transform: uppercase; white-space: nowrap; }
  .excerpt { font-size: 10.2px; line-height: 15.7px; color: var(--text); white-space: nowrap; }
  .meta { font-size: 6.6px; line-height: 10.5px; color: #444; }
  .meta b { font-weight: 600; color: #222; }
</style>
</head>
<body>

<header>
  <div class="abs topbar">
    <p class="abs info" style="left:254px"><strong>Monday - Friday 13:30 - 17:30</strong><br>Saturday and Sunday closed</p>
    <span class="abs divider" style="left:381px"></span>
    <p class="abs info" style="left:403px"><strong>0555 210 7394</strong><br><strong>info@varlowgfc.com</strong></p>
    <span class="abs divider" style="left:508px"></span>
    <p class="abs info" style="left:534px"><strong>Lorem ipsum dolor sit amet, consectetur adipiscing<br>elit. Sed semper massa sit amet</strong></p>
    <a class="abs appointment">MAKE AN APPOINTMENT</a>
  </div>

  <nav class="abs nav">
    <div class="abs brand">
      <span class="brand-mark"></span>
      <span class="brand-name">Varlow</span>
    </div>
    <div class="menu">
      <a style="left:615px">Home</a>
      <a style="left:683px">About</a>
      <a style="left:751px">Programs</a>
      <a class="active" style="left:820px">Blog</a>
      <a style="left:901px">Contact</a>
    </div>
  </nav>
</header>

<section class="abs hero" role="img" aria-label="Athlete leaping off a wall in a dim urban alley, blue-toned">
  <h1 class="abs hero-title">LATEST NEWS</h1>
  <p class="abs hero-sub">Lorem ipsum dolor sit amet, consectetur adipiscing elit. Sed<br>semper massa sit amet urna bibendum dapibus. Nunc eleifend</p>
  <div class="abs tabs">
    <span class="abs tab" style="left:18px">SPORT</span>
    <span class="abs tab" style="left:181px">NUTRITION</span>
    <span class="abs tab" style="left:343px">FITNESS</span>
    <span class="abs tab" style="left:506px">GYMNASTICS</span>
    <span class="abs tab-line"></span>
  </div>
</section>

<main>
  <article class="abs card" style="left:254px;top:542px;width:689px;height:293px">
    <div class="photo" role="img" aria-label="Runner mid-leap on a track beside a concrete wall under a grey sky"
      style="left:0;top:0;width:452px;height:293px;background:linear-gradient(180deg,#6e6f73 0%,#8a8b8e 55%,#6f6a55 78%,#5c4a3c 100%)"></div>
    <div class="abs" style="left:476px;top:18px;width:200px">
      <h2 class="title">When to run<br>fast</h2>
      <p class="excerpt" style="margin-top:2px">Lorem ipsum dolor sit amet,<br>consectetur adipisicing elit, sed do<br>eiusmod tempor incididunt ut labore<br>et dolore magna aliqua. Ut enim ad<br>minim veniam, quis nostrud<br>exercitation ullamco laboris nisi ut<br>aliquip ex ea commodo consequat.<br>Duis aute irure dolor in reprehenderit<br>in voluptate velit esse cillum</p>
      <p class="excerpt" style="margin-top:15.7px">dolore eu fugiat nulla pariatur.</p>
      <p class="meta" style="margin-top:30px"><b>By Varlow</b><br>March 24, 2017</p>
    </div>
  </article>

  <article class="abs card" style="left:254px;top:850px;width:218px;height:321px">
    <div class="photo" role="img" aria-label="Woman lifting dumbbells in a dark gym"
      style="left:0;top:0;width:218px;height:164px;background:linear-gradient(110deg,#1a1a1a 0%,#2a2a2a 60%,#4a3a32 100%)"></div>
    <div class="abs" style="left:17px;top:184px;width:195px">
      <h2 class="title">Overcome<br>mental block</h2>
      <p class="excerpt" style="margin-top:2px">Lorem ipsum dolor sit amet,<br>consectetur adipiscing elit. Integer<br>imperdiet iaculis ipsum aliquet</p>
      <p class="meta" style="margin-top:14px"><b>By Varlow</b><br>March 24, 2017</p>
    </div>
  </article>

  <article class="abs card" style="left:489px;top:850px;width:217px;height:179px">
    <div class="abs" style="left:14px;top:14px;width:195px">
      <h2 class="title">Stay with the<br>plan</h2>
      <p class="excerpt" style="margin-top:12px;padding-left:2px">Lorem ipsum dolor sit amet,<br>consectetur adipiscing elit. Integer<br>imperdiet iaculis ipsum aliquet<br>ultricies. Sed a tincidunt enim.</p>
      <p class="meta" style="margin-top:22px;padding-left:2px"><b>By Varlow</b><br>March 24, 2017</p>
    </div>
  </article>

  <div class="abs photo" role="img" aria-label="Basketball player holding a ball on an outdoor court"
    style="left:489px;top:1044px;width:217px;height:156px;background:linear-gradient(180deg,#7d8a86 0%,#b9c4c6 45%,#6f8f86 100%)"></div>

  <article class="abs card" style="left:726px;top:850px;width:217px;height:294px">
    <div class="photo" role="img" aria-label="Close-up of hands checking a smartwatch, bright blue sleeve"
      style="left:0;top:0;width:217px;height:164px;background:linear-gradient(135deg,#e6e9ec 0%,#c8d4da 45%,#3aa6dc 80%,#1e8fd0 100%)"></div>
    <div class="abs" style="left:15px;top:184px;width:200px">
      <h2 class="title">Win 1 month free<br>membership</h2>
      <p class="excerpt" style="margin-top:2px;padding-left:1px">Lorem ipsum dolor sit amet,<br>consectetur adipiscing elit. Integer</p>
      <p class="meta" style="margin-top:12px;padding-left:1px"><b>By Varlow</b><br>March 24, 2017</p>
    </div>
  </article>

  <article class="abs card" style="left:726px;top:1160px;width:217px;height:60px">
    <h2 class="abs title" style="left:14px;top:12px;width:200px">What now, after<br>training</h2>
  </article>
</main>

</body>
</html>
```